Tech Startup wants A4 and A3 Poster

We need an A4 and an A3 Poster for a new company in Australia called 'tolmu'. tolmu has created a personal safety app that records videos that are synchronised with the cloud. It also integrates your location. We want to have posters for the purpose of advertising. We would prefer if you looked at our website www.tolmu-example.com and even download the plain square badge app at https://apps.example-store.net/details?id=com.orvex.tolmu and kept the theme we have used. The Poster should communicate in very terms what our product does with a focus on people downloading the app. Please find our logo attached.

Industry/Entity Type

Safety

```html
<!DOCTYPE html>
<html lang="en">
<head>
<meta charset="utf-8">
<title>tolmu – Personal safety app poster</title>
<link rel="stylesheet" href="https://fonts.googleapis.com/css2?family=Quicksand:wght@400;500&family=Roboto:wght@400;500&display=swap">
<style>
  :root {
    --brand-blue: #1174ba;
    --appbar-blue: #2b80c8;
    --statusbar-blue: #1966aa;
    --white: #ffffff;
    --ink: #333333;
    --muted: #8a8a8a;
    --divider: #e4e4e4;
    --device: #161616;
    --thumb-warm: #b0614e;
    --thumb-dark: #5a3a2c;
    --shadow: rgba(0, 0, 0, 0.14);
  }
  * { box-sizing: border-box; margin: 0; padding: 0; }
  html, body { width: 848px; height: 1200px; overflow: hidden; background: var(--white); }
  .poster {
    position: relative; width: 848px; height: 1200px; overflow: hidden;
    font-family: "Quicksand", sans-serif; background: var(--white);
  }
  .intro {
    position: absolute; top: 0; left: 0; width: 100%; height: 166px;
    background: var(--brand-blue); color: var(--white);
    display: flex; align-items: center; justify-content: center;
    text-align: center; font-size: 24px; font-weight: 500; line-height: 30px;
  }
  .hero { position: absolute; top: 166px; left: 0; width: 100%; height: 601px; overflow: hidden; }
  .brand-area {
    position: absolute; left: 76px; top: 85px; width: 336px; height: 336px;
    border-radius: 50%; background: var(--brand-blue);
  }
  .brand-shadow {
    position: absolute; left: 60px; top: 496px; width: 368px; height: 14px;
    border-radius: 50%; background: radial-gradient(ellipse at center, var(--shadow), transparent 70%);
  }
  .brand-name {
    position: absolute; left: 460px; top: 14px;
    font-size: 100px; font-weight: 400; color: var(--brand-blue); letter-spacing: 1px;
  }
  .tagline {
    position: absolute; left: 462px; top: 130px;
    font-size: 60px; font-weight: 400; line-height: 56px; color: var(--brand-blue);
  }
  .availability {
    position: absolute; left: 462px; top: 266px;
    display: flex; align-items: center; gap: 18px;
    font-size: 21px; font-weight: 500; color: var(--brand-blue);
  }
  .store-badge { width: 30px; height: 34px; border-radius: 5px; background: var(--brand-blue); }
  .device {
    position: absolute; left: 466px; top: 316px; width: 308px; height: 420px;
    background: var(--device); border-radius: 30px;
  }
  .device-speaker { position: absolute; left: 116px; top: 26px; width: 76px; height: 6px; border-radius: 3px; background: #2c2c2c; }
  .device-camera { position: absolute; left: 52px; top: 22px; width: 12px; height: 12px; border-radius: 50%; background: #2c2c2c; }
  .screen { position: absolute; left: 11px; top: 48px; width: 286px; height: 380px; background: #fafafa; font-family: "Roboto", sans-serif; }
  .status-bar {
    height: 23px; background: var(--statusbar-blue); color: var(--white);
    display: flex; align-items: center; justify-content: flex-end; padding: 0 10px; gap: 6px; font-size: 13px;
  }
  .app-bar {
    height: 46px; background: var(--appbar-blue); color: var(--white);
    display: flex; align-items: center; padding: 0 12px; gap: 18px; font-size: 17px;
  }
  .app-bar .title { flex: 1; }
  .count { font-size: 11px; color: var(--ink); padding: 13px 0 12px 12px; border-bottom: 1px solid var(--divider); }
  .entry { display: flex; align-items: center; height: 58px; border-bottom: 1px solid var(--divider); padding: 0 10px 0 4px; }
  .thumb { width: 50px; height: 50px; border-radius: 50%; flex: none; position: relative; }
  .thumb-a { background: linear-gradient(135deg, var(--thumb-warm), #e8d2c6); }
  .thumb-b { background: linear-gradient(135deg, var(--thumb-dark), var(--thumb-warm)); }
  .thumb-mark { position: absolute; right: -2px; top: 0; width: 16px; height: 16px; border-radius: 50%; }
  .entry-text { flex: 1; padding-left: 12px; line-height: 15px; }
  .entry-date { font-size: 11px; color: var(--ink); }
  .entry-place { font-size: 10.5px; color: var(--muted); white-space: nowrap; overflow: hidden; }
  .entry-menu { color: var(--muted); font-size: 16px; }
  .features {
    position: absolute; top: 767px; left: 0; width: 100%; height: 433px;
    background: var(--brand-blue); color: var(--white);
  }
  .feature { position: absolute; top: 72px; width: 220px; text-align: center; }
  .feature-icon { display: block; margin: 0 auto; height: 100px; }
  .feature-label { margin-top: 40px; font-size: 30px; font-weight: 400; line-height: 36px; }
  .feature-video { left: 70px; }
  .feature-location { left: 314px; }
  .feature-cloud { left: 558px; }
  .web-address { position: absolute; bottom: 58px; width: 100%; text-align: center; font-size: 36px; font-weight: 400; }
</style>
</head>
<body>
<main class="poster">
  <header class="intro">
    <p>Have you ever felt unsafe, threatened, or been bullied?<br>Maybe you simply want a better way to create, manage,<br>and store your video content?</p>
  </header>

  <section class="hero">
    <div class="brand-area" role="img" aria-label="tolmu brand mark area"></div>
    <div class="brand-shadow"></div>
    <h1 class="brand-name">tolmu</h1>
    <h2 class="tagline">Personal<br>safety app</h2>
    <div class="availability"><span>Now available on:</span><span class="store-badge" aria-label="App store"></span></div>

    <div class="device">
      <span class="device-camera"></span><span class="device-speaker"></span>
      <div class="screen">
        <div class="status-bar"><span>▾ ▮</span><span>12:46</span></div>
        <div class="app-bar">
          <svg width="18" height="18" viewBox="0 0 18 18"><path d="M16 9H3M8 3L2 9l6 6" fill="none" stroke="#fff" stroke-width="2"/></svg>
          <span class="title">tolmu</span>
          <svg width="18" height="18" viewBox="0 0 18 18"><circle cx="9" cy="5" r="4" fill="#fff"/><path d="M1 18c0-5 4-7 8-7s8 2 8 7z" fill="#fff"/></svg>
          <svg width="18" height="18" viewBox="0 0 18 18"><circle cx="9" cy="9" r="6" fill="none" stroke="#fff" stroke-width="3" stroke-dasharray="3 2"/><circle cx="9" cy="9" r="3.5" fill="none" stroke="#fff" stroke-width="2"/></svg>
        </div>
        <div class="count">33 videos</div>
        <div class="entry">
          <div class="thumb thumb-a" role="img" aria-label="Video thumbnail"><span class="thumb-mark" style="background:#2b80c8"></span></div>
          <div class="entry-text"><div class="entry-date">11 Oct 2014 03:53</div><div class="entry-place">18 Marlow Lane Kestrel VIC...</div></div>
          <span class="entry-menu">⋮</span>
        </div>
        <div class="entry">
          <div class="thumb thumb-b" role="img" aria-label="Video thumbnail"><span class="thumb-mark" style="background:#4caf50"></span></div>
          <div class="entry-text"><div class="entry-date">24 Aug 2014 08:21</div><div class="entry-place">41 Harlan Street Brimley...</div></div>
          <span class="entry-menu">⋮</span>
        </div>
        <div class="entry">
          <div class="thumb thumb-a" role="img" aria-label="Video thumbnail"><span class="thumb-mark" style="background:#4caf50"></span></div>
        </div>
      </div>
    </div>
  </section>

  <section class="features">
    <div class="feature feature-video">
      <svg class="feature-icon" viewBox="0 0 112 100" width="112"><g fill="none" stroke="#fff" stroke-width="5"><rect x="3" y="3" width="106" height="94"/><rect x="26" y="3" width="60" height="94"/></g><g fill="#fff"><rect x="9" y="12" width="11" height="9"/><rect x="9" y="33" width="11" height="9"/><rect x="9" y="55" width="11" height="9"/><rect x="9" y="77" width="11" height="9"/><rect x="92" y="12" width="11" height="9"/><rect x="92" y="33" width="11" height="9"/><rect x="92" y="55" width="11" height="9"/><rect x="92" y="77" width="11" height="9"/></g></svg>
      <p class="feature-label">Video<br>Recording</p>
    </div>
    <div class="feature feature-location">
      <svg class="feature-icon" viewBox="0 0 90 116" width="80"><path d="M45 112C30 88 4 66 4 44a41 41 0 0 1 82 0c0 22-26 44-41 68z" fill="none" stroke="#fff" stroke-width="5" stroke-linejoin="round"/><circle cx="45" cy="42" r="17" fill="none" stroke="#fff" stroke-width="5"/></svg>
      <p class="feature-label">Location<br>History</p>
    </div>
    <div class="feature feature-cloud">
      <svg class="feature-icon" viewBox="0 0 134 100" width="134"><path d="M30 92h76a25 25 0 0 0 2-50A36 36 0 0 0 40 32 30 30 0 0 0 30 92z" fill="none" stroke="#fff" stroke-width="5" stroke-linejoin="round"/></svg>
      <p class="feature-label">Sync<br>to Cloud</p>
    </div>
    <p class="web-address">www.tolmu-example.com</p>
  </section>
</main>
</body>
</html>
```